BrightHarbor, LLC
BrightHarbor
Creative Brief
Professional
Joan Ferris
Executive & Clinical Director
7183 Marbrook Avenue St. Louis, MO 63902
jferris@brightharborcare.example
www.brightharborcare.example
Card # 2 Nora Whitfield Marketing & Operations Director 7183 Marbrook Avenue St. Louis, MO 63902 Office Tel: 314-555-0172 Cell Tel: 314-555-0198 nwhitfield42@brightharborcare.example www.brightharborcare.example
WE APPRECIATE REFERRALS

```html
<!DOCTYPE html>
<html lang="en">
<head>
<meta charset="utf-8">
<title>BrightHarbor, LLC – Business Card</title>
<link href="https://fonts.googleapis.com/css2?family=Open+Sans:wght@400;600;700&display=swap" rel="stylesheet">
<style>
  :root {
    --bg: #e6e4e1;
    --card: #ffffff;
    --orange: #f39a1e;
    --grey: #8d8e90;
    --grey-dark: #6f7072;
    --grey-light: #c9cacc;
    --text: #5a5b5d;
  }
  * { box-sizing: border-box; margin: 0; padding: 0; }
  html, body { width: 1200px; height: 904px; overflow: hidden; }
  body {
    background: var(--bg);
    font-family: "Open Sans", Arial, sans-serif;
    position: relative;
  }
  .card {
    position: absolute;
    left: 250px;
    width: 700px;
    height: 400px;
    background: var(--card);
    border-radius: 18px;
    overflow: hidden;
    box-shadow: 0 6px 18px rgba(0,0,0,0.15);
  }
  .card--front { top: 34px; }
  .card--back { top: 470px; }

  .front-mark {
    position: absolute;
    left: 0; right: 0; top: 168px;
    display: flex; align-items: center; justify-content: center; gap: 12px;
  }
  .mark-dot {
    width: 34px; height: 34px; border-radius: 50%;
    background: var(--orange);
  }
  .mark-name {
    font-weight: 600; font-size: 34px; color: var(--grey-dark);
  }

  .band {
    position: absolute; left: 0; top: 0; width: 700px; height: 400px;
  }

  .back-brand {
    position: absolute; left: 34px; top: 82px;
  }
  .back-brand .brand-row { display: flex; align-items: center; gap: 8px; }
  .back-brand .mark-dot { width: 22px; height: 22px; }
  .back-brand .mark-name { font-size: 24px; }
  .tagline {
    margin-top: 2px; margin-left: 30px;
    font-size: 9px; letter-spacing: 1px; color: var(--orange);
  }

  .address {
    position: absolute; left: 34px; top: 172px;
    font-size: 14px; line-height: 20px; color: #fff;
  }
  .contacts {
    position: absolute; left: 34px; top: 228px;
    list-style: none;
    font-size: 13.5px; line-height: 19px; color: #fff;
  }
  .contacts li { display: flex; align-items: center; gap: 10px; }
  .contacts svg { width: 12px; height: 12px; fill: var(--orange); flex: none; }

  .person {
    position: absolute; left: 410px; top: 190px; color: #fff;
  }
  .person-name { font-size: 22px; font-weight: 700; }
  .person-title { font-size: 14px; }

  .website {
    position: absolute; left: 0; right: 0; bottom: 22px; text-align: center;
    font-size: 17px; letter-spacing: 1px; color: var(--grey);
  }
  .website strong { color: var(--orange); font-weight: 600; }

  .corner-mark {
    position: absolute; right: 28px; top: 34px;
    display: flex; align-items: center; gap: 8px;
  }
  .corner-mark .mark-dot { width: 20px; height: 20px; }
  .corner-mark .mark-name { font-size: 16px; color: var(--grey-dark); }
</style>
</head>
<body>

<section class="card card--front" aria-label="Card front">
  <div class="front-mark">
    <span class="mark-dot"></span>
    <span class="mark-name">BrightHarbor</span>
  </div>
</section>

<section class="card card--back" aria-label="Card back">
  <svg class="band" viewBox="0 0 700 400" aria-hidden="true">
    <defs>
      <linearGradient id="bandFill" x1="0" x2="1" y1="0" y2="0">
        <stop offset="0" stop-color="#b9babc"/>
        <stop offset="0.55" stop-color="#8d8e90"/>
        <stop offset="1" stop-color="#7b7c7e"/>
      </linearGradient>
    </defs>
    <path d="M0 160 L470 160 Q560 150 700 70 L700 340 L0 340 Z" fill="url(#bandFill)"/>
    <path d="M470 160 Q560 150 700 70 L700 92 Q570 170 480 176 Z" fill="#ffffff" opacity="0.85"/>
  </svg>

  <div class="back-brand">
    <div class="brand-row">
      <span class="mark-dot"></span>
      <span class="mark-name">BrightHarbor, LLC</span>
    </div>
    <p class="tagline">Compassionate Home Care Services</p>
  </div>

  <p class="address">7183 Marbrook Avenue<br>St. Louis, MO 63902</p>

  <ul class="contacts">
    <li><svg viewBox="0 0 12 12"><rect x="1" y="3" width="10" height="8" rx="1"/><rect x="3" y="0" width="6" height="3" rx="1"/></svg>314-555-0172</li>
    <li><svg viewBox="0 0 12 12"><rect x="3" y="0" width="6" height="12" rx="1.5"/></svg>314-555-0134</li>
    <li><svg viewBox="0 0 12 12"><rect x="1" y="2" width="10" height="9" rx="1"/></svg>314-555-0157</li>
    <li><svg viewBox="0 0 12 12"><path d="M0 2h12v8H0z"/></svg>jferris@brightharborcare.example</li>
  </ul>

  <div class="corner-mark">
    <span class="mark-dot"></span>
    <span class="mark-name">BrightHarbor</span>
  </div>

  <div class="person">
    <p class="person-name">Joan Ferris</p>
    <p class="person-title">Executive &amp; Clinical Director</p>
  </div>

  <p class="website">www.<strong>brightharborcare</strong>.example</p>
</section>

</body>
</html>
```